Carrowfield Hotel

A Hotel (Pub) in Sydney CBD. Posters will be outside of Hotel informing People what is on in Hotel.
We will be Printing in A1 size.
CARROWFIELD HOTEL
Open 9am - 3am 7 Days
Monday - Thursday
Happy Hour
4pm - 6pm
Local Beer & Wine
Wednesday
Poker Night: Great $$$ Prizes
Everyday
Steak or Schniztels: Served with Mashed Potato & Salad or Chips & Salad - $8.50
Live Sport on the Big Screen
BISTRO
OPEN 7 DAYS 12- 9pm
Daily Blackboard Specials + Full Menu Inside
Best service in Town
Target Market(s)
Male or Female 18 to Seniors.Passing Trade.
Industry/Entity Type
Hotel
Look and feel
Each slider illustrates characteristics of the customer's brand and the style your logo design should communicate.

```html
<!DOCTYPE html>
<html lang="en">
<head>
<meta charset="utf-8">
<title>Carrowfield Hotel – What's On</title>
<link rel="stylesheet" href="https://fonts.googleapis.com/css2?family=Open+Sans:wght@400;700;800&family=Chewy&family=Gochi+Hand&family=Alfa+Slab+One&display=swap">
<style>
  :root {
    --bg-light: #b3763c;
    --bg-mid: #8a5227;
    --bg-dark: #4a2a12;
    --white: #ffffff;
    --green-top: #d9f75a;
    --green-bottom: #5fbf1e;
    --poker-top: #e0288a;
    --poker-bottom: #6a1fa0;
    --gold: #e9c64a;
    --gold-dark: #9a6f12;
    --sign-gold: #b48a2a;
    --sign-gold-light: #d5ab45;
    --badge-blue: #2f8fe0;
    --badge-blue-dark: #0e4fa8;
    --chalk: #f2f2ee;
    --board: #1d1f1e;
    --wood: #d9a468;
    --wood-dark: #a56d35;
    --yellow: #ffe11a;
    --bistro-red: #c4161c;
    --band: #3a2410;
    --band-text: #c9a06a;
  }
  * { margin: 0; padding: 0; box-sizing: border-box; }
  html, body { width: 849px; height: 1200px; overflow: hidden; background: var(--bg-dark); }
  .poster {
    position: relative;
    width: 849px; height: 1200px; overflow: hidden;
    font-family: "Open Sans", Arial, sans-serif;
    color: var(--white);
  }
  .poster-background {
    position: absolute; inset: 0;
    background: radial-gradient(ellipse at 45% 42%, var(--bg-light) 0%, var(--bg-mid) 55%, var(--bg-dark) 100%);
  }
  .abs { position: absolute; white-space: nowrap; }
  .shadow { text-shadow: 2px 3px 4px rgba(0,0,0,.55); }

  .hotel-name { left: 30px; top: 80px; line-height: 1; }
  .hotel-name-text { font-weight: 400; font-size: 42px; letter-spacing: 1px; color: var(--white); }

  .open-sign { left: 455px; top: 18px; width: 380px; height: 270px; }
  .open-sign-text {
    position: absolute; left: 475px; top: 118px; width: 330px;
    text-align: center; transform: rotate(4deg);
    font-weight: 700; color: var(--white); line-height: 1.05;
    text-shadow: 1px 2px 2px rgba(0,0,0,.45);
  }
  .open-sign-text .open-word { font-size: 44px; letter-spacing: 2px; }
  .open-sign-text .open-hours { font-size: 36px; }

  .day-label { font-weight: 800; font-size: 31px; }
  .monday { left: 20px; top: 254px; }
  .happy-hour {
    left: 22px; top: 296px;
    font-family: "Chewy", "Comic Sans MS", cursive; font-size: 104px; line-height: 1.1; letter-spacing: 2px;
    background: linear-gradient(var(--green-top), var(--green-bottom));
    -webkit-background-clip: text; background-clip: text; color: transparent;
    filter: drop-shadow(3px 4px 3px rgba(0,0,0,.55));
  }
  .happy-details { left: 30px; top: 420px; font-size: 31px; font-weight: 800; }
  .hand { font-family: "Gochi Hand", "Comic Sans MS", cursive; font-weight: 400; }
  .happy-details .hand { font-size: 38px; }

  .wednesday { right: 37px; top: 468px; }
  .poker-night {
    right: 26px; top: 500px;
    font-family: "Chewy", "Comic Sans MS", cursive; font-size: 96px; line-height: 1.1; letter-spacing: 2px;
    background: linear-gradient(var(--poker-top), var(--poker-bottom));
    -webkit-background-clip: text; background-clip: text; color: transparent;
    filter: drop-shadow(3px 4px 3px rgba(0,0,0,.55));
  }
  .prizes { left: 417px; top: 626px; font-size: 44px; }
  .prizes .dollars {
    font-family: "Alfa Slab One", Georgia, serif; font-size: 58px; color: var(--gold);
    -webkit-text-stroke: 1px var(--gold-dark); letter-spacing: -2px;
  }

  .everyday { left: 22px; top: 656px; font-size: 40px; }

  .blackboard {
    position: absolute; left: -4px; top: 735px; width: 340px; height: 240px;
    background: linear-gradient(135deg, var(--wood), var(--wood-dark));
    border-radius: 4px; box-shadow: 3px 5px 10px rgba(0,0,0,.55);
  }
  .blackboard-surface {
    position: absolute; left: 22px; top: 20px; right: 20px; bottom: 20px;
    background: var(--board); color: var(--chalk);
    font-family: "Gochi Hand", "Comic Sans MS", cursive;
  }
  .board-title { position: absolute; left: 16px; top: 12px; font-size: 34px; line-height: 1.15; }
  .board-title span { display: block; padding-left: 50px; }
  .board-note { position: absolute; left: 16px; top: 108px; font-size: 18px; line-height: 1.35; }

  .price-badge { left: 238px; top: 656px; width: 165px; height: 165px; z-index: 2; }
  .price-text {
    left: 260px; top: 712px; width: 120px; text-align: center; z-index: 3;
    font-size: 36px; font-weight: 800; transform: rotate(-10deg);
    text-shadow: 1px 2px 3px rgba(0,0,0,.5);
  }

  .live-sports { left: 24px; top: 980px; font-size: 31px; font-weight: 800; }
  .big-screen { left: 225px; top: 1018px; font-size: 36px; color: var(--yellow); }

  .bistro {
    right: 30px; top: 788px;
    font-family: "Alfa Slab One", Georgia, serif; font-size: 62px; letter-spacing: 2px;
    color: var(--bistro-red);
    -webkit-text-stroke: 6px var(--white); paint-order: stroke fill;
    filter: drop-shadow(2px 4px 3px rgba(0,0,0,.5));
  }
  .bistro-hours { right: 30px; top: 878px; font-size: 31px; font-weight: 800; }
  .bistro-specials { right: 30px; top: 930px; font-size: 34px; text-align: right; line-height: 1.9; }

  .service-band {
    position: absolute; left: 0; bottom: 0; width: 849px; height: 105px;
    background: linear-gradient(var(--band), #24150a);
    border-top: 2px solid rgba(255,255,255,.12);
    display: flex; align-items: center; justify-content: center;
  }
  .service-text {
    font-family: "Alfa Slab One", Georgia, serif; font-size: 50px; letter-spacing: 2px;
    color: var(--band-text); text-shadow: 2px 3px 0 rgba(0,0,0,.6);
  }
</style>
</head>
<body>
<main class="poster">
  <div class="poster-background" role="img" aria-label="Warm brown sunburst background radiating from the centre"></div>

  <div class="abs hotel-name"><span class="hotel-name-text">Carrowfield Hotel</span></div>

  <svg class="abs open-sign" viewBox="0 0 380 270" aria-hidden="true">
    <defs>
      <linearGradient id="signFill" x1="0" y1="0" x2="0" y2="1">
        <stop offset="0" stop-color="#d5ab45"/>
        <stop offset="1" stop-color="#b48a2a"/>
      </linearGradient>
    </defs>
    <path d="M195 8 L40 95 M195 8 L355 110" stroke="#5a3a1a" stroke-width="2" fill="none"/>
    <g transform="rotate(4 190 175)">
      <rect x="12" y="90" width="356" height="172" rx="12" fill="#e8e8e8" stroke="#777" stroke-width="2"/>
      <rect x="24" y="102" width="332" height="148" rx="6" fill="url(#signFill)" stroke="#6b4d12" stroke-width="2"/>
    </g>
    <circle cx="195" cy="8" r="8" fill="#ddd" stroke="#888" stroke-width="1.5"/>
  </svg>
  <div class="open-sign-text">
    <div class="open-word">OPEN</div>
    <div class="open-hours">9am - 3am</div>
    <div class="open-hours">7 days</div>
  </div>

  <div class="abs day-label monday shadow">Monday - Thursday</div>
  <div class="abs happy-hour">Happy Hour</div>
  <div class="abs happy-details shadow">4pm - 6pm <span class="hand">Local beer &amp; wine</span></div>

  <div class="abs day-label wednesday shadow">Wednesday</div>
  <div class="abs poker-night">Poker night</div>
  <div class="abs prizes hand shadow">Great <span class="dollars">$$</span>s prizes</div>

  <div class="abs everyday day-label shadow">Everyday</div>

  <div class="blackboard">
    <div class="blackboard-surface">
      <div class="board-title">Steak or<span>Schniztels</span></div>
      <div class="board-note">Served with<br>Mashed Potato &amp; Salad or<br>Chips &amp; Salad</div>
    </div>
  </div>

  <svg class="abs price-badge" viewBox="0 0 100 100" aria-hidden="true">
    <defs>
      <radialGradient id="badgeFill" cx="40%" cy="35%" r="70%">
        <stop offset="0" stop-color="#7cc4ff"/>
        <stop offset="0.55" stop-color="#2f8fe0"/>
        <stop offset="1" stop-color="#0e4fa8"/>
      </radialGradient>
    </defs>
    <polygon fill="url(#badgeFill)" points="50,2 56,13 66,5 69,17 80,13 79,25 91,25 86,36 97,40 89,49 97,58 86,63 91,74 79,75 80,87 69,83 66,95 56,87 50,98 44,87 34,95 31,83 20,87 21,75 9,74 14,63 3,58 11,49 3,40 14,36 9,25 21,25 20,13 31,17 34,5 44,13"/>
  </svg>
  <div class="abs price-text">$8.50</div>

  <div class="abs live-sports shadow">+ live sports on</div>
  <div class="abs big-screen hand shadow">Big Screen</div>

  <div class="abs bistro">BISTRO</div>
  <div class="abs bistro-hours shadow">OPEN 7 DAYS 12- 9pm</div>
  <div class="abs bistro-specials hand shadow">Daily Blackboard Specials<br>+ Full Menu Inside</div>

  <footer class="service-band"><span class="service-text">BEST SERVICE IN TOWN</span></footer>
</main>
</body>
</html>
```